Stationery Refresh For Local Mortgage Broker

We want to modernise and standardise our stationery, including: letterhead, presentation folder, email signature and business card.

The new stationery should be a more modern and professional take on our existing colour scheme and brand. (We do not want a complete overhaul.) A folder of approved stock photos can be found here: https://filebox.example-share.net/f/7kQzR2mTn4vWx9Lp3Yb8-HsdJe5Uc1Ga/view

Our current website is: www.brindlecovefin.com.au but we will be updating this to be consistent with our new stationery.

We are open to *very slight* tweaks to our logo if you feel it needs modernising, but overall we would like to maintain consistent colour scheme.

> Letterhead

148 Calloway Parade,
Geelong, VIC, 3220
ABN: 31 805 249 067
Australian Credit License: 718293

(03) 5391 6084
www.brindlecovefin.com.au

> Presentation Folder

148 Calloway Parade,
Geelong, VIC, 3220
(03) 5391 6084
www.brindlecovefin.com.au

ABN: 31 805 249 067

> Email Signature

Liam Tresidder
Director
M. 0412 857 294
P. (03) 5391 6084
www.brindlecovefin.com.au
148 Calloway Parade,
Geelong, VIC, 3220

ABN: 31 805 249 067

(you can also include a photo if you like: https://brindlecovefin.com.au/wp-content/uploads/2020/12/Liam-Tresidder.png.webp)

> Business Card

Liam Tresidder
Director
M. 0412 857 294
P. (03) 5391 6084
www.brindlecovefin.com.au
148 Calloway Parade,
Geelong, VIC, 3220

ABN: 31 805 249 067

Additional information...

If it's useful/relevant, the services we offer are: Home Loans, Investment Loans, Refinance, Debt Consolidation, Commercial Finance, Vehicle Loans
(You may choose to use this in any of the designs)

Target Market(s)

Home Buyers and Investors

Industry/Entity Type

Mortgage broking/property/real estate

Requirements
Must have
• At least somewhat consistent with our current site (yet meaningfully modernized)
Should not have
• dramatically different logo or colourscheme overhauls

```html
<!DOCTYPE html>
<html lang="en">
<head>
<meta charset="utf-8">
<title>Brindle Cove Financial Services — Stationery</title>
<link href="https://fonts.googleapis.com/css2?family=Montserrat:wght@400;600&display=swap" rel="stylesheet">
<style>
:root{
  --brand-red:#b9282f;
  --brand-red-light:#cf4a4f;
  --brand-grey:#5c5c60;
  --paper:#ffffff;
  --backdrop:#c8c8ca;
  --ink-soft:#8a8a8e;
}
*{box-sizing:border-box;margin:0;padding:0}
html,body{width:1200px;height:904px;overflow:hidden}
body{background:var(--backdrop);font-family:'Montserrat',sans-serif;position:relative;color:var(--brand-grey)}

/* wordmark */
.wordmark{text-align:center;font-weight:400;line-height:1}
.wordmark .name{display:block;letter-spacing:.28em;text-transform:uppercase}
.wordmark .tag{display:block;letter-spacing:.3em;text-transform:uppercase;margin-top:.55em}
.wordmark--red{color:var(--brand-red)}
.wordmark--white{color:var(--paper)}

/* letterhead */
.letterhead{position:absolute;left:40px;top:30px;width:340px;height:481px;background:var(--paper);box-shadow:0 4px 14px rgba(0,0,0,.25)}
.letterhead__header{position:absolute;top:22px;left:0;right:0;display:flex;align-items:center}
.letterhead__rule{height:4px;flex:1}
.letterhead__rule--grey{background:var(--brand-grey)}
.letterhead__rule--red{background:var(--brand-red)}
.letterhead__header .wordmark{padding:0 8px}
.letterhead__header .name{font-size:13px}
.letterhead__header .tag{font-size:5.5px;color:var(--ink-soft)}
.letterhead__footer{position:absolute;left:0;right:0;bottom:0}
.letterhead__contact{font-size:5px;padding:0 6px 4px;white-space:nowrap;color:var(--brand-grey)}
.letterhead__contact .dot{color:var(--brand-red)}
.letterhead__bar{height:14px;display:flex}
.letterhead__bar-grey{flex:1;background:var(--brand-grey)}
.letterhead__bar-red{width:110px;background:var(--brand-red);color:var(--paper);font-size:5.5px;display:flex;align-items:center;justify-content:center}

/* folder */
.folder{position:absolute;left:420px;top:30px;width:740px;height:524px;display:flex;box-shadow:0 6px 18px rgba(0,0,0,.3)}
.folder__panel{position:relative;width:370px;height:524px;background:linear-gradient(160deg,var(--brand-red-light),var(--brand-red) 60%);overflow:hidden}
.folder__panel--back{border-right:1px solid rgba(0,0,0,.15)}
.hex{position:absolute}
.folder__panel--back .wordmark{position:absolute;left:22px;top:70px}
.folder .name{font-size:14px}
.folder .tag{font-size:6px}
.services{position:absolute;left:20px;top:382px;width:230px;color:var(--paper);font-size:9px;font-weight:600}
.services__title{margin-left:82px;margin-bottom:6px;border-left:2px solid var(--paper);padding-left:6px}
.services__grid{display:grid;grid-template-columns:repeat(3,1fr);gap:8px 6px}
.services__item{border-left:2px solid var(--paper);padding-left:6px;line-height:1.1}
.folder__address{position:absolute;left:20px;bottom:22px;color:var(--paper);font-size:8px;line-height:1.7}
.folder__address .pin{display:inline-block;vertical-align:middle;margin-right:3px}
.folder__panel--front .wordmark{position:absolute;right:24px;top:300px}
.folder__band{position:absolute;left:0;right:0;bottom:40px;height:20px;background:linear-gradient(#fff,#dcdcdc)}

/* business cards */
.card{position:absolute;width:330px;height:190px;border-radius:10px;overflow:hidden;box-shadow:0 5px 14px rgba(0,0,0,.28)}
.card--front{left:40px;top:620px;background:linear-gradient(160deg,var(--brand-red-light),var(--brand-red));display:flex;flex-direction:column;align-items:center;justify-content:center}
.card--front .name{font-size:16px}
.card--front .tag{font-size:7px}
.card__web{color:var(--paper);font-size:8px;font-weight:600;margin-top:18px}
.card--back{left:400px;top:620px;background:var(--paper);display:flex}
.card--back .wordmark{width:150px;align-self:center}
.card--back .name{font-size:11px}
.card--back .tag{font-size:5px;color:var(--ink-soft)}
.card__divider{width:1px;background:var(--brand-grey);margin:40px 0}
.card__details{padding:34px 0 0 16px;font-size:8px;line-height:1.6}
.card__person{color:var(--brand-red);font-weight:600;font-size:11px}
.card__role{margin-bottom:6px}
.card__stripe{position:absolute;left:0;right:0;bottom:0;height:8px;display:flex}
.card__stripe span{flex:1}

/* notebook */
.notebook{position:absolute;left:900px;top:590px;width:220px;height:290px;border-radius:6px;overflow:hidden;background:var(--brand-red);box-shadow:0 5px 14px rgba(0,0,0,.28)}
.notebook__photo{position:absolute;left:0;top:0;width:220px;height:100px}
.notebook .wordmark{position:absolute;left:0;right:0;top:148px}
.notebook .name{font-size:13px}
.notebook .tag{font-size:5.5px}
.notebook__band{position:absolute;left:0;right:0;bottom:30px;height:10px;background:linear-gradient(#fff,#ddd)}
.notebook__strap{position:absolute;right:36px;top:0;bottom:0;width:7px;background:var(--brand-grey)}
</style>
</head>
<body>

<!-- Letterhead -->
<section class="letterhead" aria-label="Letterhead">
  <div class="letterhead__header">
    <span class="letterhead__rule letterhead__rule--grey"></span>
    <div class="wordmark wordmark--red"><span class="name">Brindle Cove</span><span class="tag">Financial Services</span></div>
    <span class="letterhead__rule letterhead__rule--red"></span>
  </div>
  <div class="letterhead__footer">
    <p class="letterhead__contact"><span class="dot">●</span> 148 Calloway Parade, Geelong, VIC, 3220 <span class="dot">●</span> ABN: 31 805 249 067 <span class="dot">●</span> Australian Credit License: 718293 <span class="dot">●</span> (03) 5391 6084</p>
    <div class="letterhead__bar"><span class="letterhead__bar-grey"></span><span class="letterhead__bar-red">www.brindlecovefin.com.au</span></div>
  </div>
</section>

<!-- Presentation folder -->
<section class="folder" aria-label="Presentation folder">
  <div class="folder__panel folder__panel--back">
    <div class="wordmark wordmark--white"><span class="name">Brindle Cove</span><span class="tag">Financial Services</span></div>
    <svg class="hex" style="left:210px;top:40px" width="130" height="112" viewBox="0 0 130 112" role="img" aria-label="Photo: parent lifting a child outside a family home"><polygon points="32,3 98,3 127,56 98,109 32,109 3,56" fill="#d8cfc2" stroke="#fff" stroke-width="5"/></svg>
    <svg class="hex" style="left:150px;top:180px" width="140" height="120" viewBox="0 0 140 120" role="img" aria-label="Photo: palm-lined waterfront under blue sky"><defs><linearGradient id="water" x1="0" y1="0" x2="0" y2="1"><stop offset="0" stop-color="#6fa9dc"/><stop offset="1" stop-color="#1d5b8c"/></linearGradient></defs><polygon points="35,3 105,3 137,60 105,117 35,117 3,60" fill="url(#water)" stroke="#fff" stroke-width="5"/></svg>
    <svg class="hex" style="left:230px;top:290px" width="130" height="112" viewBox="0 0 130 112" role="img" aria-label="Photo: weatherboard house with white picket fence"><polygon points="32,3 98,3 127,56 98,109 32,109 3,56" fill="#cfd4d6" stroke="#fff" stroke-width="5"/></svg>
    <div class="services">
      <p class="services__title">Services</p>
      <div class="services__grid">
        <span class="services__item">Home Loans</span>
        <span class="services__item">Investment Loans</span>
        <span class="services__item">Refinance</span>
        <span class="services__item">Commercial Finance</span>
        <span class="services__item">Vehicle Loans</span>
        <span class="services__item">Debt Consolidation</span>
      </div>
    </div>
    <p class="folder__address">
      <svg class="pin" width="7" height="9" viewBox="0 0 7 9"><path d="M3.5 0A3.5 3.5 0 0 0 0 3.5C0 6 3.5 9 3.5 9S7 6 7 3.5A3.5 3.5 0 0 0 3.5 0z" fill="#fff"/></svg>148 Calloway Parade, Geelong, VIC, 3220 · (03) 5391 6084 · www.brindlecovefin.com.au<br>
      ABN: 31 805 249 067 · Australian Credit License: 718293
    </p>
  </div>
  <div class="folder__panel folder__panel--front">
    <svg class="hex" style="left:30px;top:40px" width="130" height="112" viewBox="0 0 130 112" role="img" aria-label="Photo: timber homes along a quiet street"><polygon points="32,3 98,3 127,56 98,109 32,109 3,56" fill="#c9d3cf" stroke="#fff" stroke-width="5"/></svg>
    <svg class="hex" style="left:120px;top:140px" width="130" height="112" viewBox="0 0 130 112" role="img" aria-label="Photo: friends sharing a meal outdoors"><polygon points="32,3 98,3 127,56 98,109 32,109 3,56" fill="#9aa88a" stroke="#fff" stroke-width="5"/></svg>
    <svg class="hex" style="left:40px;top:245px" width="140" height="120" viewBox="0 0 140 120" role="img" aria-label="Photo: curved seawall and pier on the bay"><defs><linearGradient id="bay" x1="0" y1="0" x2="0" y2="1"><stop offset="0" stop-color="#b7c9d8"/><stop offset="1" stop-color="#3f6c8a"/></linearGradient></defs><polygon points="35,3 105,3 137,60 105,117 35,117 3,60" fill="url(#bay)" stroke="#fff" stroke-width="5"/></svg>
    <div class="wordmark wordmark--white"><span class="name">Brindle Cove</span><span class="tag">Financial Services</span></div>
    <div class="folder__band"></div>
  </div>
</section>

<!-- Business card front -->
<section class="card card--front" aria-label="Business card front">
  <div class="wordmark wordmark--white"><span class="name">Brindle Cove</span><span class="tag">Financial Services</span></div>
  <p class="card__web">www.brindlecovefin.com.au</p>
</section>

<!-- Business card back -->
<section class="card card--back" aria-label="Business card back">
  <div class="wordmark wordmark--red"><span class="name">Brindle Cove</span><span class="tag">Financial Services</span></div>
  <span class="card__divider"></span>
  <div class="card__details">
    <p class="card__person">Liam Tresidder</p>
    <p class="card__role">Director</p>
    <p>148 Calloway Parade,<br>Geelong, VIC, 3220</p>
    <p>P. (03) 5391 6084</p>
    <p>M. 0412 857 294</p>
    <p>ABN: 31 805 249 067</p>
    <p>Australian Credit License: 718293</p>
  </div>
  <div class="card__stripe"><span style="background:var(--brand-grey)"></span><span style="background:var(--brand-red)"></span></div>
</section>

<!-- Notebook cover -->
<section class="notebook" aria-label="Notebook cover">
  <svg class="notebook__photo" viewBox="0 0 220 100" preserveAspectRatio="none" role="img" aria-label="Photo: family standing in front of a new home"><defs><linearGradient id="home" x1="0" y1="0" x2="0" y2="1"><stop offset="0" stop-color="#dfe4e2"/><stop offset="1" stop-color="#8ea48a"/></linearGradient></defs><path d="M0 0H220V70Q110 40 0 80Z" fill="url(#home)"/></svg>
  <div class="wordmark wordmark--white"><span class="name">Brindle Cove</span><span class="tag">Financial Services</span></div>
  <div class="notebook__band"></div>
  <div class="notebook__strap"></div>
</section>

</body>
</html>
```